Cloud Hosted Phone System for small and medium sized businesses

I want to design a one A4 page size single or double sided brochure to offer cloud hosted VoIP Phone system and a complete collaboration system. We have partnered with a VoIP Phone system company and want to sell their services but we don't want their name to be shown on the brochure because customers might call them directly. The company name is our (www.zelvora-example.com) and our company name is HALCYON Tech Solutions. I have also uploaded my compnay's logo that you should show on the brochure. For more details about the product, you can visit their website as mentioned above.

Target Market(s)

Small and medium sized business including law firms, marketing and advertising agencies, real-estate firms and others.

Industry/Entity Type

Voip

Colors

Designer to choose colors to be used in the design.

Requirements
Must have
• My company's Logo (HALCYON Tech Solutions). Price list, services and some images to show the benefits and services of the cloud based and advanced VoIP phone system. I want the brochure to look very professional and attractive.
• Contact US: Our company's name, Logo, web address, phone (416-557-9086) and email (info@halcyontechsolutions-example.com)
Nice to have
• It is a Canadian based company and all of our servers and customers’ data reside in Canada.

```html
<!DOCTYPE html>
<html lang="en">
<head>
<meta charset="utf-8">
<title>HALCYON Tech Solutions – Cloud-Based Phone System Brochure</title>
<link href="https://fonts.googleapis.com/css2?family=Montserrat:wght@400;500;600;700;800&family=Roboto:wght@300;400;500;700&display=swap" rel="stylesheet">
<style>
:root{
  --blue:#1560b0;
  --blue-bright:#1d86d8;
  --navy:#0f3463;
  --ink:#1b1d22;
  --grey-text:#3b3f46;
  --dark:#24272b;
  --light:#eef0f2;
  --row:#d9dbde;
  --white:#ffffff;
  --backdrop:#8a8c8f;
}
*{box-sizing:border-box;margin:0;padding:0}
html,body{width:1200px;height:782px;overflow:hidden;background:var(--backdrop)}
body{font-family:"Roboto",sans-serif;color:var(--ink);position:relative}
.page{position:absolute;top:34px;width:482px;height:696px;background:var(--white);overflow:hidden;box-shadow:0 6px 18px rgba(0,0,0,.35)}
.page--front{left:66px}
.page--back{left:630px}
.abs{position:absolute}

/* brand block */
.brand{display:flex;align-items:center;gap:8px}
.brand__dot{width:42px;height:42px;border-radius:50%;background:var(--blue);flex:none}
.brand__name{font-family:"Montserrat",sans-serif;font-weight:600;color:var(--navy);font-size:28px;line-height:1;letter-spacing:.5px}
.brand__sub{font-family:"Montserrat",sans-serif;font-weight:600;color:var(--navy);font-size:13px;line-height:1.1;margin-top:2px}

/* front header */
.front-head{left:0;top:0;width:482px;height:85px;background:var(--white)}
.front-head .brand{position:absolute;left:150px;top:18px}
.notch{left:229px;top:84px;width:0;height:0;border-left:12px solid transparent;border-right:12px solid transparent;border-top:12px solid var(--white);z-index:3}

/* hero */
.hero{left:0;top:85px;width:482px;height:285px;background:linear-gradient(100deg,#16263d 0%,#1b3556 45%,#25507e 100%)}
.hero__visual{position:absolute;left:250px;top:0;width:232px;height:285px;background:radial-gradient(circle at 45% 45%,#4a86c2 0%,#2a5a8e 35%,#1a3456 70%,transparent 100%)}
.hero__title{position:absolute;left:30px;top:24px;font-family:"Montserrat",sans-serif;font-size:28px;line-height:1.15}
.hero__title .accent{color:var(--blue-bright);font-weight:700;display:block}
.hero__title .rest{color:var(--white);font-weight:400;display:block}
.hero__rule{position:absolute;left:31px;top:125px;width:38px;height:3px;background:var(--blue-bright)}
.hero__copy{position:absolute;left:31px;top:150px;width:212px;color:#e6ecf3;font-size:8.3px;line-height:1.35;text-align:justify}
.hero__copy p+p{margin-top:7px}

/* benefits */
.benefits__title{left:30px;top:386px;font-family:"Montserrat",sans-serif;font-size:18.5px;font-weight:700;color:var(--ink);letter-spacing:-.2px;white-space:nowrap}
.benefits__title span{color:var(--blue);font-weight:500}
.benefit{left:0;width:482px}
.benefit__bar{position:absolute;left:4px;top:10px;width:44px;height:16px;background:var(--navy)}
.benefit__icon{position:absolute;left:30px;top:0;width:36px;height:36px;border-radius:50%;background:var(--blue);border:3px solid var(--white);box-shadow:0 0 0 1px #c9ced6}
.benefit__icon svg{position:absolute;left:7px;top:7px}
.benefit__head{position:absolute;left:76px;top:-4px;font-family:"Montserrat",sans-serif;font-size:9.5px;font-weight:700;color:var(--blue)}
.benefit__text{position:absolute;left:76px;top:9px;width:392px;font-size:7px;line-height:1.3;color:var(--grey-text);text-align:justify}

/* front footer */
.front-foot{left:0;top:638px;width:482px;height:58px;background:var(--blue)}
.front-foot__label{position:absolute;left:0;width:482px;top:10px;text-align:center;color:var(--white);font-size:11px}
.contact-row{position:absolute;left:0;width:482px;top:31px;display:flex;justify-content:center;gap:9px;color:var(--white);font-size:8.2px;white-space:nowrap}
.contact-row span{display:flex;align-items:center;gap:4px}
.dot-icon{width:8px;height:8px;border-radius:50%;background:var(--white);display:inline-block;flex:none}

/* back top */
.back-title{left:0;width:482px;top:25px;text-align:center;font-family:"Montserrat",sans-serif;font-size:15.5px;color:var(--navy);font-weight:500}
.back-title b{color:var(--blue);font-weight:700}
.offer{top:68px;width:118px;text-align:center}
.offer svg{display:block;margin:0 auto 6px}
.offer__name{font-size:10px;line-height:1.25;color:var(--ink);font-weight:500}
.offer__name em{font-style:normal;color:var(--blue)}
.offer__text{font-size:7.6px;line-height:1.35;color:var(--grey-text);margin-top:6px}

/* features */
.features{left:0;top:212px;width:482px;height:200px;background:linear-gradient(180deg,#2b2e33 0%,#1f2226 60%,#3a3e44 100%)}
.features__pill{left:152px;top:196px;width:178px;height:28px;border-radius:14px;background:var(--navy);border:2px solid var(--white);color:var(--white);font-family:"Montserrat",sans-serif;font-size:14px;text-align:center;line-height:24px;z-index:2}
.features__pill b{font-weight:700}
.feature-list{list-style:none;color:var(--white);font-size:10px;line-height:16.6px}
.feature-list li{display:flex;align-items:center;gap:8px}
.feature-list li::before{content:"";width:6px;height:6px;border-radius:50%;border:1.5px solid var(--blue-bright);flex:none}
.feature-list li.more::before{visibility:hidden}

/* plans */
.plans{left:0;top:412px;width:482px;height:218px;background:var(--light)}
.plans__title{left:20px;top:446px;font-family:"Montserrat",sans-serif;font-size:20px;color:var(--blue);font-weight:400}
.plans__title b{font-weight:700}
.plan-head{top:434px;height:40px;background:var(--blue);color:var(--white);font-size:10px;font-weight:500;text-align:center;display:flex;align-items:center;justify-content:center;line-height:1.15}
.cell{height:19px;font-size:7.6px;display:flex;align-items:center}
.cell--label{left:20px;width:164px;padding-left:8px;color:var(--ink)}
.cell--label.grey{background:var(--row)}
.cell--label.indent{padding-left:22px}
.cell--val{justify-content:center;color:var(--ink)}
.cell--val.on{background:var(--blue);color:var(--white)}

/* back footer */
.back-foot{left:0;top:630px;width:482px;height:66px;background:var(--white)}
.back-foot .brand{position:absolute;left:24px;top:14px}
.back-foot .brand__dot{width:36px;height:36px}
.back-foot .brand__name{font-size:23px}
.back-foot .brand__sub{font-size:11px}
.contact-tag{left:190px;top:653px;width:72px;height:22px;background:var(--blue);color:var(--white);font-size:10px;line-height:22px;text-align:center;transform:skewX(-14deg);z-index:2}
.contact-tag span{display:inline-block;transform:skewX(14deg)}
.contact-panel{left:232px;top:630px;width:250px;height:66px;background:var(--dark);clip-path:polygon(14% 0,100% 0,100% 100%,0 100%)}
.contact-stack{left:272px;top:639px;color:var(--white);font-size:9px;line-height:16px;white-space:nowrap}
.contact-stack div{display:flex;align-items:center;gap:6px}
</style>
</head>
<body>

<section class="page page--front">
  <header class="abs front-head">
    <div class="brand">
      <span class="brand__dot"></span>
      <div><div class="brand__name">HALCYON</div><div class="brand__sub">Tech Solutions</div></div>
    </div>
  </header>
  <div class="abs notch"></div>

  <div class="abs hero">
    <div class="hero__visual" role="img" aria-label="Photo of open hands holding a glowing cloud chip with circuit lines"></div>
    <h1 class="hero__title"><span class="accent">A Cloud-Based</span><span class="rest">Phone System</span><span class="rest">For Businesses</span></h1>
    <div class="hero__rule"></div>
    <div class="hero__copy">
      <p>We can help you grow your business by modernizing your company's phone system and making it easy to use, manage, and track directly from the cloud</p>
      <p>Our cloud business phone system adapts to your economic challenges and brings flexibility and adaptability to your business communications whilst considerably reducing costs compared to traditional phone systems. We take great pride in continually improving our platform as well as developing new features and services that in turn increase our customers' productivity.</p>
    </div>
  </div>

  <h2 class="abs benefits__title">BENEFITS OF <span>CLOUD-BASED PHONE SYSTEM</span></h2>

  <div class="abs benefit" style="top:424px">
    <div class="benefit__bar"></div>
    <div class="benefit__icon"><svg width="16" height="16" viewBox="0 0 16 16"><rect x="4.5" y="1" width="7" height="14" rx="1.5" fill="none" stroke="#fff" stroke-width="1.4"/><circle cx="8" cy="12.5" r=".9" fill="#fff"/></svg></div>
    <div class="benefit__head">BECOME MOBILE</div>
    <p class="benefit__text">From our cloud-based telephony and its unified communications system emerges the concept of mobility. Make calls using your office phone, computer, or mobile phone, and chat with your colleagues and customers from numerous locations. Enjoy centralized communications and simplified management.</p>
  </div>

  <div class="abs benefit" style="top:474px">
    <div class="benefit__bar"></div>
    <div class="benefit__icon"><svg width="16" height="16" viewBox="0 0 16 16"><ellipse cx="8" cy="9" rx="6" ry="4.5" fill="#fff"/><rect x="5" y="12" width="2" height="3" fill="#fff"/><rect x="9" y="12" width="2" height="3" fill="#fff"/><rect x="6.5" y="4" width="3" height="1" fill="#fff"/></svg></div>
    <div class="benefit__head">SAVE COSTS</div>
    <p class="benefit__text">The fixed and operating costs of your business communications are substantially reduced, and we take care of installing, configuring, and managing your phone system. Call us today for free consultation</p>
  </div>

  <div class="abs benefit" style="top:516px">
    <div class="benefit__bar"></div>
    <div class="benefit__icon"><svg width="16" height="16" viewBox="0 0 16 16"><path d="M3 4c0 5 4 9 9 9l1.5-2-2.5-2-1.5 1C8 9 7 8 6 6.5l1-1.5-2-2.5z" fill="#fff"/><path d="M9 3a4 4 0 0 1 4 4M9 1a6 6 0 0 1 6 6" fill="none" stroke="#fff" stroke-width="1.1"/></svg></div>
    <div class="benefit__head">STAY ABREAST</div>
    <p class="benefit__text">Enjoy leading-edge telecommunications technology and its host of features that adapt to your needs, whatever the size of your business. These features are constantly upscaled and automatically updated. You will thus never have to operate an obsolete system.</p>
  </div>

  <div class="abs benefit" style="top:564px">
    <div class="benefit__bar"></div>
    <div class="benefit__icon"><svg width="16" height="16" viewBox="0 0 16 16"><path d="M4 12a3 3 0 0 1 0-6 4 4 0 0 1 7.6-1A3.5 3.5 0 0 1 12 12z" fill="#fff"/></svg></div>
    <div class="benefit__head">AVOID INCONVENIENCES</div>
    <p class="benefit__text">We take charge of the structure of your business phone system and remove the PBX (Private Branch Exchange) system to host it in its cloud database, thus saving you space, time, and costs. You are cleared of wire clutter and your business communications are streamlined, allowing you to work freely and efficiently. Also, this service includes an excellent recovery and business continuity plan that prevents unforeseen events, such as claims or system failures, from leading to data loss or suspension of business activities.</p>
  </div>

  <footer class="abs front-foot">
    <div class="front-foot__label">Contact Us:</div>
    <div class="contact-row">
      <span><i class="dot-icon"></i>416-557-9086</span>
      <span><i class="dot-icon"></i>www.halcyontechsolutions-example.com</span>
      <span><i class="dot-icon"></i>info@halcyontechsolutions-example.com</span>
    </div>
  </footer>
</section>

<section class="page page--back">
  <h2 class="abs back-title"><b>A CLOUD-BASED PHONE SYSTEM</b> FOR BUSINESSES</h2>

  <div class="abs offer" style="left:4px">
    <svg width="38" height="38" viewBox="0 0 38 38"><rect x="6" y="14" width="22" height="18" rx="3" fill="none" stroke="#555" stroke-width="1.6"/><rect x="10" y="18" width="6" height="10" fill="#777"/><path d="M20 6a6 6 0 0 1 11 2 5 5 0 0 1 0 10H22" fill="none" stroke="#555" stroke-width="1.4"/></svg>
    <div class="offer__name"><em>Cloud Phone</em><br>System</div>
    <p class="offer__text">Your business phone system, now in the cloud. Access every feature from anywhere.</p>
  </div>
  <div class="abs offer" style="left:124px">
    <svg width="38" height="38" viewBox="0 0 38 38"><rect x="8" y="5" width="24" height="26" fill="none" stroke="#555" stroke-width="1.6"/><line x1="8" y1="11" x2="32" y2="11" stroke="#555" stroke-width="1.4"/><path d="M16 34v-12l3-3 3 3v12" fill="none" stroke="#555" stroke-width="1.4"/></svg>
    <div class="offer__name"><em>Unified</em><br>Communications</div>
    <p class="offer__text">A powerful suite of communications and collaboration tools grouped under one platform.</p>
  </div>
  <div class="abs offer" style="left:244px">
    <svg width="38" height="38" viewBox="0 0 38 38"><circle cx="19" cy="19" r="2" fill="#555"/><g stroke="#555" stroke-width="1.2" fill="none"><path d="M19 17V8M19 21v9M17 19H7M21 19h10"/><rect x="15" y="3" width="8" height="5"/><rect x="2" y="16" width="5" height="6"/><rect x="31" y="16" width="5" height="6"/><rect x="15" y="30" width="8" height="5"/></g></svg>
    <div class="offer__name"><em>Contact</em><br>Center</div>
    <p class="offer__text">Manage your different customer contact points from a unified, user-friendly web interface.</p>
  </div>
  <div class="abs offer" style="left:364px">
    <svg width="38" height="38" viewBox="0 0 38 38"><path d="M9 20a10 10 0 0 1 20 0" fill="none" stroke="#555" stroke-width="1.6"/><rect x="6" y="18" width="5" height="8" rx="2" fill="#555"/><rect x="27" y="18" width="5" height="8" rx="2" fill="#555"/><path d="M29 26c0 4-4 6-9 6" fill="none" stroke="#555" stroke-width="1.4"/></svg>
    <div class="offer__name"><em>Meet</em><br>Console©</div>
    <p class="offer__text">A flexible yet easy-to-use online administration portal to manage your business phone system.</p>
  </div>

  <div class="abs features" role="img" aria-label="Dark photo of city office towers behind the feature list"></div>
  <div class="abs features__pill"><b>INCLUDED</b> FEATURES</div>
  <ul class="abs feature-list" style="left:52px;top:225px">
    <li>Access to our online portal</li>
    <li>Company greeting message (24h/7)</li>
    <li>Company's directory</li>
    <li>Company and user voicemail</li>
    <li>Outbound Caller ID</li>
    <li>Voicemail to email</li>
    <li>Call Forwarding</li>
    <li>Find-me/Follow-me</li>
    <li>Call waiting</li>
  </ul>
  <ul class="abs feature-list" style="left:272px;top:225px">
    <li>Automatic phone relocation</li>
    <li>Remote office calling &amp; transfering</li>
    <li>Phone queueing service</li>
    <li>Fraud Monitoring</li>
    <li>Custom Music on Hold</li>
    <li>Optional Hidden Caller ID</li>
    <li>Authorization code before dialing</li>
    <li>Remote Answer</li>
    <li>Call recording</li>
    <li class="more">...and more!</li>
  </ul>

  <div class="abs plans" role="img" aria-label="Faded photo of people working at an office desk"></div>
  <h2 class="abs plans__title"><b>SERVICE</b> PLANS</h2>
  <div class="abs plan-head" style="left:186px;width:94px">BASIC</div>
  <div class="abs plan-head" style="left:282px;width:96px;background:#1a6cc2">★BEST SELLER★<br>ENHANCED</div>
  <div class="abs plan-head" style="left:380px;width:78px">PREMIUM</div>

  <div class="abs cell cell--label grey" style="top:478px">MONTHLY ACCOUNT FEE<sup>1</sup>(per site)</div>
  <div class="abs cell cell--val on" style="top:478px;left:186px;width:94px">$ 45,00</div>
  <div class="abs cell cell--val on" style="top:478px;left:282px;width:96px">$ 45,00</div>
  <div class="abs cell cell--val on" style="top:478px;left:380px;width:78px">$ 45,00</div>

  <div class="abs cell cell--label grey" style="top:500px">MONTHLY USER FEE STARTING AT :</div>

  <div class="abs cell cell--label grey indent" style="top:522px">0 to 19 users</div>
  <div class="abs cell cell--val on" style="top:522px;left:186px;width:94px">$ 18,00</div>
  <div class="abs cell cell--val on" style="top:522px;left:282px;width:96px">$ 20,00</div>
  <div class="abs cell cell--val on" style="top:522px;left:380px;width:78px">$ 22,00</div>

  <div class="abs cell cell--label indent" style="top:541px">20 to 49 users</div>
  <div class="abs cell cell--val" style="top:541px;left:186px;width:94px">$ 15,00</div>
  <div class="abs cell cell--val" style="top:541px;left:282px;width:96px">$ 17,00</div>
  <div class="abs cell cell--val" style="top:541px;left:380px;width:78px">$ 19,00</div>

  <div class="abs cell cell--label grey indent" style="top:560px">50 to 99 users</div>
  <div class="abs cell cell--val on" style="top:560px;left:186px;width:94px">$ 12,00</div>
  <div class="abs cell cell--val on" style="top:560px;left:282px;width:96px">$ 14,00</div>
  <div class="abs cell cell--val on" style="top:560px;left:380px;width:78px">$ 16,00</div>

  <div class="abs cell cell--label indent" style="top:579px">100 to 199 users</div>
  <div class="abs cell cell--val" style="top:579px;left:186px;width:94px">$ 10,00</div>
  <div class="abs cell cell--val" style="top:579px;left:282px;width:96px">$ 12,00</div>
  <div class="abs cell cell--val" style="top:579px;left:380px;width:78px">$ 14,00</div>

  <div class="abs cell cell--label grey indent" style="top:598px">200+ users</div>
  <div class="abs cell cell--val on" style="top:598px;left:186px;width:94px">$ 8,00</div>
  <div class="abs cell cell--val on" style="top:598px;left:282px;width:96px">$ 10,00</div>
  <div class="abs cell cell--val on" style="top:598px;left:380px;width:78px">$ 12,00</div>

  <footer class="abs back-foot">
    <div class="brand">
      <span class="brand__dot"></span>
      <div><div class="brand__name">HALCYON</div><div class="brand__sub">Tech Solutions</div></div>
    </div>
  </footer>
  <div class="abs contact-panel"></div>
  <div class="abs contact-tag"><span>Contact Us:</span></div>
  <div class="abs contact-stack">
    <div><i class="dot-icon"></i>416-557-9086</div>
    <div><i class="dot-icon"></i>info@halcyontechsolutions-example.com</div>
    <div><i class="dot-icon"></i>www.halcyontechsolutions-example.com</div>
  </div>
</section>

</body>
</html>
```